Redesign Website for Tandara Flame

I have an existing website on https://www.tandaraflame-example.com.au/ and would like to have this redesigned professionally with new content (please refer to word document). We are fire protection engineers providing fire services design expertise and engineering design to a range of different clients.

We also provide drafting services to clients in the form of completing final commissioning documentation such as 'as-installed' drawings and fire services block plans to ensure compliance with the building code and relevant Australian Standards.

Target Market(s)

Builders, Architects, Consultants, Project Managers

Industry/Entity Type

Engineering Consultant

Coding

Coded - Design and coding required

Number of Pages Required

4 page

Font styles to use
Sans Serif

Requirements
Must have
• Home and about Page, fire services design page, fire block plans page, contact us page (4 Pages).

The website colour choice must match or compliment the new company logo.
Nice to have
• Quality photos of fire services installations in buildings to Australian Standards.

A website similar to this would be ideal http://corbellpyro-example.com.au
Should not have
• Stolen licensed photos

```html
<!DOCTYPE html>
<html lang="en">
<head>
<meta charset="utf-8">
<title>Tandara Flame – Fire Services Drawings and Block Plans</title>
<link rel="stylesheet" href="https://fonts.googleapis.com/css2?family=Lato:ital,wght@0,400;0,700;0,900;1,400;1,700&family=Open+Sans:wght@700&display=swap">
<style>
:root{
  --orange:#f5821f;
  --black:#0a0a0a;
  --ink:#222;
  --text:#333;
  --grey-hex:#666666;
  --light:#efefef;
  --white:#ffffff;
}
*{box-sizing:border-box;margin:0;padding:0}
html,body{width:1200px;height:3930px;overflow:hidden}
body{position:relative;background:var(--white);font-family:'Lato',sans-serif;color:var(--text)}
.abs{position:absolute}
.brand{display:flex;align-items:center;gap:12px}
.brand-mark{width:22px;height:22px;background:var(--orange)}
.brand-name{font-family:'Lato',sans-serif;font-weight:700;color:var(--orange);font-size:26px;letter-spacing:.5px}
.site-header{left:0;top:0;width:1200px;height:134px}
.site-header .brand{left:75px;top:48px}
.main-nav{right:75px;top:57px;display:flex;gap:44px;font-weight:900;font-size:15px;color:var(--black)}
.main-nav .active{color:var(--orange)}
.hero{left:0;top:134px;width:1200px;height:710px;
  background:linear-gradient(120deg,#6b1d22 0%,#8d2a2e 25%,#4a4e63 50%,#2d3448 70%,#b9b7b0 100%);
  clip-path:polygon(0 0,1200px 0,1200px 652px,977px 652px,954px 710px,256px 710px,222px 652px,0 652px)}
.hero-title{left:0;width:1200px;top:222px;text-align:center;color:var(--white);font-weight:900;font-size:80px;letter-spacing:1px}
.hero-sub{left:0;width:1200px;top:312px;text-align:center;color:var(--white);font-family:'Open Sans',sans-serif;font-weight:700;font-size:43px}
.btn{display:flex;align-items:center;justify-content:center;font-weight:900;font-size:18px;color:var(--white)}
.btn-orange{background:var(--orange)}
.btn-black{background:var(--black)}
.hero .btn{left:498px;top:384px;width:204px;height:56px}
.hero-dots{left:560px;top:648px;display:flex;gap:9px}
.hero-dots span{width:13px;height:13px;border-radius:50%;background:var(--white)}
.hero-dots span:first-child{background:var(--orange)}
.about-photo{left:0;top:898px;width:588px;height:548px;
  background:linear-gradient(180deg,#6f8ea8 0%,#8a9aa3 45%,#5f7f86 60%,#3c5a3a 100%);
  clip-path:polygon(0 0,430px 0,588px 274px,430px 548px,0 548px)}
.section-title{color:var(--orange);font-weight:900;font-size:40px}
.about-title{left:615px;top:955px}
.about-copy{left:615px;top:1020px;width:520px;font-size:16.5px;line-height:27.5px}
.about-copy p+p{margin-top:12px}
.about .btn{left:615px;top:1319px;width:205px;height:58px}
.services{left:0;top:1504px;width:1200px;height:855px;background:var(--light)}
.services .section-title{left:0;width:1200px;top:70px;text-align:center}
.services-intro{left:75px;width:1050px;top:132px;text-align:center;font-size:16.5px;line-height:28px}
.services-lead{left:75px;top:218px;width:520px;color:var(--orange);font-style:italic;font-size:16.5px;line-height:27.5px}
.measure-list{left:75px;top:285px;width:480px;list-style:none;font-size:16.5px;line-height:28.5px}
.measure-list li{position:relative;padding-left:33px;margin-bottom:13px}
.measure-list svg{position:absolute;left:0;top:6px}
.services .btn{left:75px;top:705px;width:204px;height:57px}
.services-photo{left:617px;top:224px;width:583px;height:550px;
  background:linear-gradient(135deg,#d9dde0 0%,#c6ccd1 40%,#8c7a60 65%,#2f3542 100%);
  clip-path:polygon(113px 0,583px 0,583px 550px,113px 550px,0 275px)}
.block-plans{left:0;top:2359px;width:1200px;height:832px;
  background:linear-gradient(135deg,#f3f3f3 0%,#e6e6e6 50%,#efe9e9 100%)}
.block-plans .section-title{left:0;width:1200px;top:55px;text-align:center}
.block-intro{left:90px;width:1020px;top:116px;text-align:center;font-size:16.5px;line-height:27.5px}
.hex{width:306px;height:267px;clip-path:polygon(25% 0,75% 0,100% 50%,75% 100%,25% 100%,0 50%);
  display:flex;flex-direction:column;align-items:center;justify-content:center;color:var(--white);
  font-weight:900;font-size:22px;line-height:28px;text-align:center;text-transform:uppercase;padding:0 40px}
.hex svg{margin-bottom:14px}
.hex-grey{background:var(--grey-hex)}
.hex-black{background:var(--black)}
.hex-orange{background:var(--orange)}
.samples{left:0;top:3191px;width:1200px;height:469px;background:var(--light)}
.samples .section-title{left:0;width:1200px;top:60px;text-align:center}
.sample-card{top:135px;width:330px;height:258px;background:var(--white);border:1px solid #8a8a8a;padding:8px}
.sample-card div{width:100%;height:100%;background:linear-gradient(135deg,#f4f4f4,#dcdcdc)}
.sample-arrow{top:250px}
.site-footer{left:0;top:3660px;width:1200px;height:270px;background:var(--white)}
.site-footer .brand{left:75px;top:99px}
.brand-small .brand-name{font-size:24px}
.copyright{left:75px;top:189px;font-size:13px;line-height:21px;color:var(--text)}
.footer-head{font-weight:700;font-size:16px;color:var(--ink)}
.footer-col{top:66px}
.footer-links{list-style:none;font-size:14px;line-height:27.5px;margin-top:10px}
.contact-text{font-size:14px;line-height:22px;margin-top:12px}
.contact-row{display:flex;align-items:center;gap:18px;font-size:14px;margin-top:14px}
.social{display:flex;gap:26px;margin-top:18px}
.social span{width:22px;height:22px;border-radius:50%;background:var(--ink)}
.abn{font-weight:700;font-size:14px;margin-top:36px}
</style>
</head>
<body>

<header class="site-header abs">
  <div class="brand abs"><span class="brand-mark"></span><span class="brand-name">TANDARA FLAME</span></div>
  <nav class="main-nav abs">
    <span class="active">HOME</span><span>ABOUT</span><span>FIRE SERVICES PLANS</span><span>FIRE BLOCK PLANS</span><span>CONTACT US</span>
  </nav>
</header>

<section class="hero abs" role="img" aria-label="Photo of a technician in a yellow hard hat working on a red fire alarm control panel">
  <h1 class="hero-title abs">TANDARA FLAME</h1>
  <p class="hero-sub abs">Fire Services Drawings and Block Plans</p>
  <a class="btn btn-orange abs">READ MORE</a>
  <div class="hero-dots abs"><span></span><span></span><span></span><span></span></div>
</section>

<section class="about">
  <div class="about-photo abs" role="img" aria-label="Photo of Sydney Harbour skyline with the Opera House"></div>
  <h2 class="section-title about-title abs">ABOUT TANDARA FLAME</h2>
  <div class="about-copy abs">
    <p>Tandara Flame is a company based in Sydney, Australia providing the Australian market expertise in the field of fire safety.<br>Our mission is to assist our clients with the preparation of design and specifications of fire services upgrades and final commissioning documentation to achieve compliance with the National Construction Code (NCC) and relevant Australian Standards.</p>
    <p>We can also assist with the review and endorsement of fire services design required under the new fire safety reforms which came into effect on July 2017.</p>
  </div>
  <a class="btn btn-black abs">READ MORE</a>
</section>

<section class="services abs">
  <h2 class="section-title abs">FIRE SERVICES PLANS</h2>
  <p class="services-intro abs">Tandara Flame can assist with the preparation of the design and specification for the upgrade or installation or new fire safety&nbsp; systems to achieve compliance with the National Construction Code (NCC), Council Fire Orders or Fire Engineering Reports.</p>
  <p class="services-lead abs">We have proficient knowledge in the ability to produce design and specifications relating to the below fire safety measures:</p>
  <ul class="measure-list abs">
    <li><svg width="16" height="16" viewBox="0 0 16 16"><circle cx="8" cy="8" r="8" fill="#f5821f"/><path d="M4.5 8.2l2.3 2.3 4.7-4.7" stroke="#fff" stroke-width="2" fill="none"/></svg>Automatic Smoke Detection and Alarm System</li>
    <li><svg width="16" height="16" viewBox="0 0 16 16"><circle cx="8" cy="8" r="8" fill="#f5821f"/><path d="M4.5 8.2l2.3 2.3 4.7-4.7" stroke="#fff" stroke-width="2" fill="none"/></svg>Emergency Warning and Intercom System (EWIS) /Sound System and Intercom System for Emergency Purposes (SSISEP)</li>
    <li><svg width="16" height="16" viewBox="0 0 16 16"><circle cx="8" cy="8" r="8" fill="#f5821f"/><path d="M4.5 8.2l2.3 2.3 4.7-4.7" stroke="#fff" stroke-width="2" fill="none"/></svg>Occupant Warning System (OWS)</li>
    <li><svg width="16" height="16" viewBox="0 0 16 16"><circle cx="8" cy="8" r="8" fill="#f5821f"/><path d="M4.5 8.2l2.3 2.3 4.7-4.7" stroke="#fff" stroke-width="2" fill="none"/></svg>Smoke Alarms</li>
    <li><svg width="16" height="16" viewBox="0 0 16 16"><circle cx="8" cy="8" r="8" fill="#f5821f"/><path d="M4.5 8.2l2.3 2.3 4.7-4.7" stroke="#fff" stroke-width="2" fill="none"/></svg>Fire Hose Reels</li>
    <li><svg width="16" height="16" viewBox="0 0 16 16"><circle cx="8" cy="8" r="8" fill="#f5821f"/><path d="M4.5 8.2l2.3 2.3 4.7-4.7" stroke="#fff" stroke-width="2" fill="none"/></svg>Portable Fire Extinguishers</li>
    <li><svg width="16" height="16" viewBox="0 0 16 16"><circle cx="8" cy="8" r="8" fill="#f5821f"/><path d="M4.5 8.2l2.3 2.3 4.7-4.7" stroke="#fff" stroke-width="2" fill="none"/></svg>Fire Hydrant Systems</li>
    <li><svg width="16" height="16" viewBox="0 0 16 16"><circle cx="8" cy="8" r="8" fill="#f5821f"/><path d="M4.5 8.2l2.3 2.3 4.7-4.7" stroke="#fff" stroke-width="2" fill="none"/></svg>Emergency Lighting and Exit signs</li>
  </ul>
  <a class="btn btn-black abs">READ MORE</a>
  <div class="services-photo abs" role="img" aria-label="Photo of a technician in an orange hard hat fitting a ceiling smoke detector"></div>
</section>

<section class="block-plans abs" role="region" aria-label="Fire block plans, over a faint photo of technical drawings">
  <h2 class="section-title abs">FIRE BLOCK PLANS</h2>
  <p class="block-intro abs">We can can also assist you with the preparation of final commissioning documentation as required to achieve with relevant Australian Standards. Some of the services we provide (but not limited to) include:</p>

  <div class="hex hex-grey abs" style="left:203px;top:202px">
    <svg width="72" height="50" viewBox="0 0 72 50" fill="none" stroke="#fff" stroke-width="3"><ellipse cx="36" cy="18" rx="32" ry="12"/><path d="M6 22v8c0 7 13 12 30 12s30-5 30-12v-8"/><ellipse cx="36" cy="30" rx="12" ry="5"/></svg>
    Zone Block Plans
  </div>
  <div class="hex hex-black abs" style="left:695px;top:202px">
    <svg width="64" height="52" viewBox="0 0 64 52" fill="none" stroke="#fff" stroke-width="3"><path d="M4 18h12l14-12v40L16 34H4z"/><path d="M38 18c4 4 4 12 0 16M45 12c8 8 8 20 0 28M52 6c12 12 12 28 0 40"/></svg>
    EWIS / SSISEP Block Plans
  </div>
  <div class="hex hex-orange abs" style="left:447px;top:347px">
    <svg width="60" height="72" viewBox="0 0 60 72" fill="none" stroke="#fff" stroke-width="3"><path d="M4 4h52M12 12h36M30 12v14M20 26h20M24 26v8h12v-8"/><path d="M18 44l-6 8M30 44v12M42 44l6 8M14 62l-4 6M30 62v6M46 62l4 6" stroke-dasharray="3 3"/></svg>
    Sprinkler Block Plans
  </div>
  <div class="hex hex-black abs" style="left:203px;top:490px">
    <svg width="56" height="76" viewBox="0 0 56 76" fill="none" stroke="#fff" stroke-width="3"><path d="M28 2v8M16 20c0-8 24-8 24 0z"/><path d="M12 20h32v50H12z"/><path d="M4 34h8M44 34h8M4 28v12M52 28v12"/><circle cx="28" cy="36" r="8"/><path d="M6 72h44"/></svg>
    Fire Hydrant Block Plans
  </div>
  <div class="hex hex-grey abs" style="left:695px;top:490px">
    <svg width="60" height="60" viewBox="0 0 60 60" fill="none" stroke="#fff" stroke-width="3"><path d="M30 4h26v52H30"/><path d="M4 30h34M28 20l10 10-10 10"/></svg>
    Evacuation Management Plan Diagrams
  </div>
</section>

<section class="samples abs">
  <h2 class="section-title abs">SAMPLE WORK</h2>
  <svg class="sample-arrow abs" style="left:42px" width="18" height="32" viewBox="0 0 18 32"><path d="M16 2L2 16l14 14" stroke="#222" stroke-width="2.5" fill="none"/></svg>
  <div class="sample-card abs" style="left:75px"><div role="img" aria-label="Sample fire services block plan drawing with coloured zones"></div></div>
  <div class="sample-card abs" style="left:436px"><div role="img" aria-label="Sample site block plan drawing with a green building footprint"></div></div>
  <div class="sample-card abs" style="left:797px"><div role="img" aria-label="Sample evacuation block plan line drawing"></div></div>
  <svg class="sample-arrow abs" style="left:1140px" width="18" height="32" viewBox="0 0 18 32"><path d="M2 2l14 14L2 30" stroke="#222" stroke-width="2.5" fill="none"/></svg>
</section>

<footer class="site-footer abs">
  <div class="brand brand-small abs"><span class="brand-mark"></span><span class="brand-name">TANDARA FLAME</span></div>
  <p class="copyright abs">Copyright © 2021 CompanyName<br>All Rights Reserved</p>

  <div class="footer-col abs" style="left:363px">
    <h3 class="footer-head">SITE MAP</h3>
    <ul class="footer-links"><li>Home</li><li>About</li><li>Fire Services Plans</li><li>Fire Block Plans</li><li>Contact us</li></ul>
  </div>

  <div class="footer-col abs" style="left:597px">
    <h3 class="footer-head">CONTACT ADDRESS</h3>
    <p class="contact-text">Quis autem vel eum iure<br>reprehenderit</p>
    <div class="contact-row"><svg width="15" height="15" viewBox="0 0 24 24"><path fill="#222" d="M6.6 10.8a15 15 0 006.6 6.6l2.2-2.2c.3-.3.7-.4 1-.2 1.1.4 2.3.6 3.6.6.6 0 1 .4 1 1V20c0 .6-.4 1-1 1A17 17 0 013 4c0-.6.4-1 1-1h3.5c.6 0 1 .4 1 1 0 1.3.2 2.5.6 3.6.1.3 0 .7-.2 1z"/></svg>+614 55 010 482</div>
    <div class="contact-row"><svg width="15" height="13" viewBox="0 0 24 20"><rect x="1" y="1" width="22" height="18" fill="#222"/><path d="M2 3l10 8 10-8" stroke="#fff" stroke-width="2" fill="none"/></svg>info@tandaraflame-example.com.au</div>
  </div>

  <div class="footer-col abs" style="left:886px">
    <h3 class="footer-head">FOLLOW US</h3>
    <div class="social" aria-label="Social media links"><span></span><span></span><span></span><span></span><span></span></div>
    <p class="abn">ABN: 12 345 678 901</p>
  </div>
</footer>

</body>
</html>
```